Business Card Design Project

We need a business card design for a company based in San Francisco called PlanGlide. PlanGlide makes customized academic planners for high schools and middle schools. Currently we sell directly to the schools who either re-sell or give the planners to their students. The planners are designed to help students stay organized and manage their time. The books are unique in that they are made individually for each school and include the school's events, student artwork and most importantly the daily class schedule in each week. This helps the student to understand what classes they have each day and what homework they need to do each night.

Currently the product is B:B; however, we are exploring ways in which to make this a B:C. Please review website at www.planglide.net

The final design should communicate time management and organization.

Card should be one-sided

Information for the business card should include

Dorothy Kellner Voss
Founder
dorothy@planglide.net
415-836-1752

Target Market(s)

High school and middle school administrators

Industry/Entity Type

School

Requirements
Must have
• One sided design
Nice to have
• I'm open to new interpretations of the logo as well as color usage. I'm also open to changing the font of the logo type.
Should not have
• Please use a san serif font.

```html
<!DOCTYPE html>
<html lang="en">
<head>
<meta charset="utf-8">
<title>PlanGlide — Business Card</title>
<link rel="stylesheet" href="https://fonts.googleapis.com/css2?family=Source+Sans+3:wght@400;600&display=swap">
<style>
  :root {
    --backdrop: #8b8b8b;
    --card-top: #ffffff;
    --card-bottom: #d9d9d9;
    --ink: #1d1b1c;
    --brand-red: #c41e27;
    --band-black: #231f20;
    --rule: #111111;
  }
  * { margin: 0; padding: 0; box-sizing: border-box; }
  html, body {
    width: 1200px; height: 750px; overflow: hidden;
    background: var(--backdrop);
    font-family: "Source Sans 3", sans-serif;
  }
  .business-card {
    position: absolute; left: 150px; top: 118px;
    width: 900px; height: 514px;
    background: linear-gradient(170deg, var(--card-top) 0%, #eeeeee 55%, var(--card-bottom) 100%);
    box-shadow: 0 8px 22px rgba(0,0,0,0.35);
    overflow: hidden;
  }
  .brand { position: absolute; left: 62px; top: 64px; }
  .brand-name {
    font-size: 46px; font-weight: 400; color: var(--ink);
    letter-spacing: -0.5px; line-height: 1;
  }
  .brand-tagline {
    margin-top: 2px; margin-left: 22px;
    font-size: 17px; color: var(--brand-red); letter-spacing: 0.2px;
  }
  .person { position: absolute; left: 176px; top: 300px; }
  .person-name {
    font-size: 30px; font-weight: 600; color: var(--brand-red); line-height: 1.1;
  }
  .person-title { font-size: 21px; color: var(--ink); margin-left: 18px; margin-top: 2px; }
  .divider {
    position: absolute; left: 196px; top: 384px;
    width: 676px; height: 2px; background: var(--rule);
    transform: rotate(-3.2deg); transform-origin: left center;
  }
  .contact {
    position: absolute; right: 28px; top: 380px;
    text-align: right; font-size: 20px; color: var(--ink); line-height: 1.4;
  }
  .contact-line { display: flex; align-items: center; justify-content: flex-end; gap: 12px; }
  .contact-icon { width: 20px; height: 16px; fill: var(--brand-red); }
  .card-band { position: absolute; left: 0; bottom: 0; width: 900px; height: 40px; }
</style>
</head>
<body>
  <div class="business-card">
    <div class="brand">
      <div class="brand-name">PlanGlide</div>
      <div class="brand-tagline">Customized Academic Planners</div>
    </div>

    <div class="person">
      <div class="person-name">Dorothy Kellner Voss</div>
      <div class="person-title">Founder</div>
    </div>

    <div class="divider"></div>

    <div class="contact">
      <div class="contact-line">
        <span>415-836-1752</span>
        <svg class="contact-icon" viewBox="0 0 20 16" aria-hidden="true">
          <path d="M1 5 Q10 -1 19 5 L17 8 L14 6 L14 4 L6 4 L6 6 L3 8 Z"/>
          <rect x="4" y="8" width="12" height="7" rx="1"/>
        </svg>
      </div>
      <div class="contact-line">
        <span>dorothy@planglide.net</span>
        <svg class="contact-icon" viewBox="0 0 20 16" aria-hidden="true">
          <rect x="0" y="1" width="20" height="14" rx="1"/>
          <path d="M1 2 L10 9 L19 2" fill="none" stroke="#ffffff" stroke-width="1.5"/>
        </svg>
      </div>
    </div>

    <svg class="card-band" viewBox="0 0 900 40" preserveAspectRatio="none" aria-hidden="true">
      <polygon points="0,22 568,22 560,40 0,40" fill="var(--brand-red)"/>
      <polygon points="578,8 900,8 900,40 566,40" fill="var(--band-black)"/>
    </svg>
  </div>
</body>
</html>
```